Forest Consultant/Timber Buyer needs a clean business card

We are a forestry consulting and timber buying company. We meet with private landowners and assist them with timber management and timber harvesting. We would like a professional business card, please no clip art. logo is blue and white but would like to see a gray,silver, or some other color incorporated. Would like basic contact info. Would like to the layout to be creative and sleek but masculine.

Target Market(s)

private landowners

Industry/Entity Type

Business

Contact Information for Business Card

name,position, cell number, office number, email, website. This might be to cluttered. Basic contact info is what we are looking for.

Contact info can all be on one side with logo on the other.

Font styles to use
Serif
Sans Serif

Colors
0255a3
ffffff
aaaaaa

Requirements
Must have
• We just want it professional.
Nice to have
• Creative layout.
Should not have
• please no clip art of log trucks etc.

```html
<!DOCTYPE html>
<html lang="en">
<head>
<meta charset="utf-8">
<title>Ridgeway Forestry Group – Business Card</title>
<link rel="stylesheet" href="https://fonts.googleapis.com/css2?family=Roboto:wght@400;500&display=swap">
<style>
  :root {
    --brand-blue: #0255a3;
    --deep-blue: #05478c;
    --white: #ffffff;
    --silver: #aaaaaa;
    --charcoal: #231f20;
    --backdrop: #3a3a3a;
  }
  html, body {
    margin: 0;
    padding: 0;
    width: 1200px;
    height: 965px;
    overflow: hidden;
    background: var(--backdrop);
    font-family: "Roboto", Arial, sans-serif;
  }
  .canvas {
    position: relative;
    width: 1200px;
    height: 965px;
  }
  .card {
    position: absolute;
    left: 246px;
    width: 710px;
    height: 404px;
    border-radius: 34px;
    overflow: hidden;
    background: linear-gradient(180deg, var(--brand-blue), var(--deep-blue));
    box-shadow: 0 6px 16px rgba(0,0,0,0.5);
  }
  .card--front { top: 60px; }
  .card--back { top: 504px; }
  .card__art {
    position: absolute;
    inset: 0;
  }
  .wordmark {
    position: absolute;
    text-align: center;
    font-weight: 500;
    line-height: 1;
  }
  .wordmark__name {
    display: block;
    font-size: 40px;
    letter-spacing: 2px;
  }
  .wordmark__tag {
    display: block;
    font-size: 12px;
    letter-spacing: 4px;
    margin-top: 9px;
  }
  .card--front .wordmark {
    left: 60px;
    width: 260px;
    top: 232px;
    color: var(--brand-blue);
  }
  .card--back .wordmark {
    left: 0;
    right: 0;
    top: 162px;
    color: var(--white);
  }
  .card--back .wordmark__name { font-size: 48px; letter-spacing: 3px; }
  .card--back .wordmark__tag { font-size: 14px; letter-spacing: 6px; margin-top: 12px; }

  .details {
    position: absolute;
    right: 56px;
    top: 72px;
    text-align: right;
    color: var(--white);
  }
  .details__name { font-size: 21px; margin: 0; line-height: 1.2; }
  .details__role { font-size: 16px; margin: 2px 0 0; }
  .contact {
    list-style: none;
    margin: 52px 0 0;
    padding: 0;
    font-size: 16.5px;
    line-height: 21px;
  }
  .contact li {
    display: flex;
    justify-content: flex-end;
    align-items: center;
    gap: 8px;
  }
  .contact svg { width: 16px; height: 16px; flex: none; }
  .address {
    margin: 50px 0 0;
    font-size: 16.5px;
    line-height: 21px;
  }
</style>
</head>
<body>
<main class="canvas">

  <section class="card card--front" aria-label="Card front">
    <svg class="card__art" viewBox="0 0 710 404" aria-hidden="true">
      <path d="M190 0 L258 0 C385 130 440 300 362 404 L350 404 C415 290 350 120 190 0 Z" fill="var(--charcoal)"/>
      <path d="M190 0 C335 110 420 270 330 404" fill="none" stroke="var(--white)" stroke-width="1.5" opacity="0.6"/>
      <defs>
        <linearGradient id="paper" x1="0" y1="0" x2="0" y2="1">
          <stop offset="0" stop-color="#ffffff"/>
          <stop offset="1" stop-color="#e2e2e2"/>
        </linearGradient>
      </defs>
      <path d="M0 0 L190 0 C330 110 400 280 312 404 L0 404 Z" fill="url(#paper)"/>
    </svg>

    <div class="wordmark">
      <span class="wordmark__name">RIDGEWAY</span>
      <span class="wordmark__tag">FORESTRY GROUP</span>
    </div>

    <div class="details">
      <p class="details__name">Daniel Hale</p>
      <p class="details__role">Managing Director</p>
      <ul class="contact">
        <li>+555 21 45 87
          <svg viewBox="0 0 16 16"><rect x="1" y="2" width="3" height="12" rx="1" fill="#fff"/><rect x="5" y="3" width="10" height="11" rx="1" fill="none" stroke="#fff" stroke-width="1.5"/><path d="M7 6h6M7 9h6M7 12h6" stroke="#fff"/></svg>
        </li>
        <li>+555 14 87 98
          <svg viewBox="0 0 16 16"><rect x="4" y="1" width="8" height="14" rx="1.5" fill="none" stroke="#fff" stroke-width="1.5"/><circle cx="8" cy="12.5" r="1" fill="#fff"/></svg>
        </li>
        <li>info@ridgeway.com
          <svg viewBox="0 0 16 16"><rect x="1" y="3" width="14" height="10" fill="#fff"/><path d="M1 3l7 6 7-6M1 13l5-5M15 13l-5-5" fill="none" stroke="var(--brand-blue)" stroke-width="1.2"/></svg>
        </li>
        <li>www.ridgeway.com
          <svg viewBox="0 0 16 16" fill="none" stroke="#fff" stroke-width="1.2"><circle cx="8" cy="8" r="6.5"/><ellipse cx="8" cy="8" rx="3" ry="6.5"/><path d="M1.5 8h13M2.5 5h11M2.5 11h11"/></svg>
        </li>
      </ul>
      <p class="address">Here your company or<br>home address</p>
    </div>
  </section>

  <section class="card card--back" aria-label="Card back">
    <div class="wordmark">
      <span class="wordmark__name">RIDGEWAY</span>
      <span class="wordmark__tag">FORESTRY GROUP</span>
    </div>
  </section>

</main>
</body>
</html>
```